Tri-fold two sided brochure for Maplebrook Ridge Home Health Care
Maplebrook Ridge Home Health Care
Tri-fold two sided brochure for Maplebrook Ridge Home Health Care - Medical
Creative Brief
Medical
Maplebrook Ridge Home Health is a full service home health agency, providing a wide range of skilled and supportive services including: Wound Care, Ostomy Care, Catheter Care, pre and post-Op Care, Medication Management, Diabetic Management, Patient and care giver training, Pain Management, Feeding Tubes, Intramuscular Injections, Subcutaneous Injections, Nutritional Counselling, Disease Management, Blood pressure Monitoring, PT/INR Monitoring, Blood Draw and IV Therapy. Our Services are as follows: Skilled Nursing Physical Therapy Occupational Therapy Speech Therapy Home health Aide Medical Social Worker Registered Dietitian
on the first page I want the logo with black or white background and a picture on the back I want pictures, address and contact numbers In the middle I want the content and the services we provide I need help with the pictures and content I just wrote some in the detail and target boxes some ideas Our target is patients who are in need of home health care but mainly their physicians are the target because patients need to get the referrals from their primary physicians, medicare and insurance companies
tulipgate42 tulipgate42
I would like the unified accreditation board logo on the first page please

```html
<!DOCTYPE html>
<html lang="en">
<head>
<meta charset="utf-8">
<title>Maplebrook Ridge Home Health – Tri-fold Brochure</title>
<link href="https://fonts.googleapis.com/css2?family=PT+Sans+Narrow:wght@400;700&family=Open+Sans:wght@400;600&display=swap" rel="stylesheet">
<style>
  :root {
    --teal: #14968a;
    --teal-dark: #0d7a70;
    --teal-light: #5fc2b6;
    --ink: #4a4f52;
    --muted: #8a8f92;
    --rule: #d6d9da;
    --paper: #ffffff;
    --backdrop: #e6e7e8;
  }
  * { box-sizing: border-box; margin: 0; padding: 0; }
  html, body { width: 1200px; height: 982px; overflow: hidden; background: var(--backdrop); }
  .brochure {
    position: absolute; left: 40px; top: 41px;
    width: 1120px; height: 900px;
    display: flex; background: var(--paper);
    box-shadow: 0 6px 24px rgba(0,0,0,.18);
  }
  .panel { position: relative; width: 373.33px; height: 100%; overflow: hidden; background: var(--paper); }
  .panel + .panel { border-left: 1px solid #eef0f0; }
  .band-bottom { position: absolute; left: 0; right: 0; bottom: 0; height: 22px; background: var(--teal); }

  /* testimonials */
  .testimonials { padding: 60px 42px 0 42px; }
  .testimonials h2 {
    font-family: "PT Sans Narrow", "Arial Narrow", sans-serif; font-weight: 700;
    color: var(--teal); font-size: 30px; line-height: 1.05; text-transform: uppercase;
    padding-left: 50px;
  }
  .quote-mark { font-family: Georgia, serif; color: var(--ink); font-size: 34px; line-height: 1; margin: 22px 0 6px 50px; }
  .review p {
    font-family: "Open Sans", Arial, sans-serif; font-size: 11.5px; line-height: 1.6;
    color: var(--muted); text-align: justify; padding-left: 50px;
  }
  .review .reviewer {
    font-family: "PT Sans Narrow", "Arial Narrow", sans-serif; font-weight: 700;
    font-size: 15px; color: var(--ink); text-transform: uppercase;
    margin: 14px 0 26px; padding: 0 0 0 50px; position: relative;
  }
  .review .reviewer::before {
    content: ""; position: absolute; left: 0; top: -6px; width: 100%; border-top: 1px solid var(--rule);
  }
  .review + .review p { margin-top: 4px; }

  /* gallery */
  .photo { position: absolute; }
  .gallery .p1 { left: 50px; top: 70px; width: 160px; height: 250px; background: linear-gradient(160deg, #f3ece6, #cfd9dc 60%, #9fc4c0); }
  .gallery .p2 { left: 210px; top: 0; width: 164px; height: 360px; background: linear-gradient(200deg, #f4f4f4, #d9e4e6 55%, #b7c7cc); }
  .gallery .p3 { left: 0; top: 330px; width: 200px; height: 300px; background: linear-gradient(140deg, #e9d8cb, #c7c9cc 55%, #9aa7ad); }
  .gallery .p4 { left: 200px; top: 360px; width: 174px; height: 380px; background: linear-gradient(170deg, #fbf6f2, #dce9ec 50%, #7fc9c6); }
  .gallery .p5 { left: 0; top: 630px; width: 200px; height: 110px; background: linear-gradient(180deg, #f1f2f2, #d7dcdd); }
  .gallery-badge {
    position: absolute; left: 110px; top: 265px; width: 150px; height: 150px; border-radius: 50%;
    background: var(--paper); display: flex; align-items: center; justify-content: center;
    font-family: "PT Sans Narrow", "Arial Narrow", sans-serif; font-size: 20px; color: var(--teal);
    text-transform: uppercase; box-shadow: 0 0 0 6px rgba(255,255,255,.6);
  }

  /* cover */
  .cover-top { position: absolute; left: 0; top: 0; width: 100%; height: 360px; }
  .brand {
    position: absolute; left: 150px; top: 110px; width: 200px;
    font-family: "PT Sans Narrow", "Arial Narrow", sans-serif; font-weight: 700;
    color: var(--paper); font-size: 26px; line-height: 1.1; text-transform: uppercase; letter-spacing: .5px;
  }
  .cover .hero { left: 0; top: 360px; width: 100%; height: 518px; background: linear-gradient(150deg, #9fd8d1, #e9eef0 45%, #f7efe8 70%, #dfe5e6); }
</style>
</head>
<body>
<main class="brochure">
  <section class="panel testimonials">
    <h2>What our clients have to say about us?</h2>
    <div class="quote-mark">“</div>
    <article class="review">
      <p>Our nurse visited every week and explained each step of my recovery with patience. The whole team felt like family, and my doctor received clear updates after every visit.</p>
      <div class="reviewer">Mr ABC - Featured Review</div>
    </article>
    <article class="review">
      <p>After surgery my mother needed wound care at home. The staff arrived on time, kept us informed, and made the whole process calm and simple for our family.</p>
      <div class="reviewer">Mr DEF - Verified Customer</div>
    </article>
    <article class="review">
      <p>Therapy sessions at home helped my father walk again within weeks. Friendly, skilled people who truly care about their patients and respect their time.</p>
      <div class="reviewer">Mr GHI Customer Since 2014</div>
    </article>
    <div class="band-bottom"></div>
  </section>

  <section class="panel gallery">
    <div class="photo p1" role="img" aria-label="Photo of a nurse holding a stethoscope"></div>
    <div class="photo p2" role="img" aria-label="Photo of a medical team walking in a hospital corridor"></div>
    <div class="photo p3" role="img" aria-label="Photo of a blood pressure check"></div>
    <div class="photo p4" role="img" aria-label="Photo of a doctor with a clipboard"></div>
    <div class="photo p5" role="img" aria-label="Photo of a caregiver's hands with a patient"></div>
    <div class="gallery-badge">Our Gallery</div>
    <div class="band-bottom"></div>
  </section>

  <section class="panel cover">
    <svg class="cover-top" viewBox="0 0 373 360" preserveAspectRatio="none" aria-hidden="true">
      <polygon points="110,0 373,0 373,360 0,360 0,250" fill="var(--teal)"/>
      <polygon points="0,250 110,0 140,0 20,360 0,360" fill="var(--teal-dark)" opacity=".35"/>
    </svg>
    <div class="brand">Maplebrook Ridge<br>Home Health</div>
    <div class="photo hero" role="img" aria-label="Photo of a smiling doctor in a white coat"></div>
    <div class="band-bottom"></div>
  </section>
</main>
</body>
</html>
```